Allied Health business card / Logo update.

Update/revitalise our logo and business cards. The logo needs to be suitable not only for business cards but stationary, website and clothing as well.

We have had the same hand logo for 16 years and have a strong brand name with this. One idea, however, was to base the idea around the similarities between the spine and bamboo. I will attach some images.

We are uncertain with colour. Initially, we thought earthy greens and greys/charcoal. However, we would also consider blue/charcoal combination.

I have attached our existing logo and this is our website. http://www.ridgewaybackclinic.com.au

Target Market(s)

General public
This is the only card

Industry/Entity Type

Health Care

Contact Information for Business Card

Ridgeway Backcare Centre
27 Hillview Road (Cnr Belford St and Hillview Rd) Elmsford Bay
5/18 Tindall St Tarrington
phone: 02 6471 2856
email: info@ridgewaybackclinic.com.au
web: ridgewaybackclinic.com.au

Martin K. Lowe
Cert. Rehab Therapist
Chiropractor
BSc(Hal)., MChirop(Wes)., MClinRehabNeuro(Cor)
MRBP, MTSKE, OLUX

Font styles to use
Serif
Sans Serif

Colors
acd037
85acd3
5c5c5c

Requirements
Must have
• Company name, Professional name with qualifications
• Contact details.

```html
<!DOCTYPE html>
<html lang="en">
<head>
<meta charset="utf-8">
<title>Ridgeway Backcare Centre – Business Card</title>
<link href="https://fonts.googleapis.com/css2?family=Merriweather:wght@700&family=Open+Sans:wght@400;600&display=swap" rel="stylesheet">
<style>
  :root {
    --green: #acd037;
    --charcoal: #5c5c5c;
    --ink: #4a4a4a;
    --paper: #ffffff;
    --backdrop: #e6e2dc;
  }
  html, body {
    margin: 0;
    width: 1200px;
    height: 1023px;
    overflow: hidden;
    background: var(--backdrop);
  }
  .card {
    position: absolute;
    left: 180px;
    top: 271px;
    width: 840px;
    height: 480px;
    background: var(--paper);
    box-shadow: 0 6px 24px rgba(0,0,0,0.18);
    font-family: "Open Sans", Arial, sans-serif;
    color: var(--ink);
    overflow: hidden;
  }
  .brand {
    position: absolute;
    left: 60px;
    top: 95px;
    display: flex;
    align-items: center;
    gap: 14px;
  }
  .brand-mark {
    width: 34px;
    height: 34px;
    border-radius: 50%;
    background: var(--green);
    flex: none;
  }
  .brand-name {
    font-size: 24px;
    font-weight: 600;
    color: var(--charcoal);
    line-height: 1.15;
    width: 220px;
  }
  .contact {
    position: absolute;
    left: 60px;
    top: 215px;
    font-size: 17px;
    line-height: 27px;
    text-align: right;
    width: 330px;
  }
  .person {
    position: absolute;
    left: 420px;
    top: 62px;
  }
  .person-name {
    font-family: "Merriweather", Georgia, serif;
    font-weight: 700;
    font-size: 26px;
    color: var(--green);
    margin: 0 0 6px;
  }
  .person-role {
    font-size: 19px;
    line-height: 28px;
    margin: 0;
  }
  .qualifications {
    position: absolute;
    left: 470px;
    top: 180px;
    font-size: 16px;
    line-height: 25px;
    margin: 0;
  }
  .address-band {
    position: absolute;
    left: 0;
    right: 0;
    top: 345px;
    height: 82px;
    background: var(--charcoal);
    color: var(--green);
    font-size: 17px;
    line-height: 26px;
    display: flex;
    flex-direction: column;
    justify-content: center;
    align-items: flex-end;
    padding-right: 40px;
    box-sizing: border-box;
  }
  .edge-stripe {
    position: absolute;
    left: 0;
    right: 0;
    top: 440px;
    height: 26px;
    background: var(--charcoal);
  }
</style>
</head>
<body>
  <main class="card">
    <div class="brand">
      <span class="brand-mark"></span>
      <span class="brand-name">Ridgeway Backcare Centre</span>
    </div>

    <div class="contact">
      <div>02 6471 2856</div>
      <div>info@ridgewaybackclinic.com.au</div>
      <div>www.ridgewaybackclinic.com.au</div>
    </div>

    <div class="person">
      <h1 class="person-name">Martin K. Lowe</h1>
      <p class="person-role">Cert. Rehab Therapist</p>
      <p class="person-role">Chiropractor</p>
    </div>

    <p class="qualifications">
      BSc(Hal)., MChirop(Wes).,<br>
      MClinRehabNeuro(Cor)<br>
      MRBP, MTSKE, OLUX
    </p>

    <div class="address-band">
      <div>27 Hillview Road (Cnr Belford St and Hillview Rd), Elmsford Bay</div>
      <div>5/18 Tindall St Tarrington</div>
    </div>

    <div class="edge-stripe"></div>
  </main>
</body>
</html>
```